Private Bar sign _ Vinyl over Perplex - Ned's Bar

We have a light box (illuminated) and need a design for it. The finished size is 1270mm wide and 270mm high.

The backgound colour is supposed to be tomato red (when lit!) so I guess the unlit colour would need to be a lot darker.

We want to have:
2 Kauriheld Bottles with the cap popping and beer squirting out
The sign to say "Ned's Bar" with a sub-line "What happens in the bar stays in the bar"

We have a 70's Juke box and it we would love it to have a bit of that theme. Not silly but rather smashing! A bit of a 3-D Look would be a real bonus. I have attached an image of what someone did for us and we hate it. They have not even cut it in nicely and applied it while we were out. Have a look at the bar and I bet you can come up with a much better sign.
Updates

Font styles to use
Script

Colors
ec1f27

Requirements
Must have
• Tomato red when illuminated
• 70's or 80's look
• 2 Kauriheld Bottles with the cap popping and beer and foam squirting out
• The sign to say "Ned's Bar" with a sub-line "What happens in the bar stays in the bar"
• Even a Pin up girl in there would not hurt!
• The writing Ned's bar should look like hand writing
• Be creative :-)
Nice to have
• A 3-D look would be awesome!
• Bold and strong colours
Should not have
• The attached sample is how we do NOT like it to look like. It is sterile. The red turns into bright orange when illuminated ( we hate orange!)

```html
<!DOCTYPE html>
<html lang="en">
<head>
<meta charset="utf-8">
<title>Ned's Bar – Light Box Sign</title>
<link rel="stylesheet" href="https://fonts.googleapis.com/css2?family=Gochi+Hand&family=Oswald:wght@500&display=swap">
<style>
  :root {
    --sign-red: #e3140f;
    --panel-red: #b80a10;
    --frame-orange: #f39020;
    --title-white: #ffffff;
    --glow-pink: #e8309a;
    --glow-magenta: #c0106e;
    --bottle-green-dark: #0f4a1a;
    --bottle-green: #2f8a34;
    --spray-amber: #f2a45a;
    --spray-foam: #fbe6cf;
  }
  html, body {
    margin: 0;
    padding: 0;
    width: 1200px;
    height: 255px;
    overflow: hidden;
    background: var(--sign-red);
  }
  .sign {
    position: relative;
    width: 1200px;
    height: 255px;
    background: var(--sign-red);
  }
  .sign__panel {
    position: absolute;
    left: 12px;
    top: 12px;
    width: 1172px;
    height: 227px;
    border: 2px solid var(--frame-orange);
    border-radius: 18px;
    background: var(--panel-red);
  }
  .sign__art {
    position: absolute;
    inset: 0;
  }
  .sign__title {
    position: absolute;
    left: 0;
    right: 0;
    top: 18px;
    margin: 0;
    text-align: center;
    font-family: "Gochi Hand", cursive;
    font-weight: 400;
    font-size: 128px;
    line-height: 1;
    letter-spacing: 6px;
    color: var(--title-white);
    text-shadow:
      3px 4px 2px #7a7a7a,
      0 0 14px var(--glow-pink),
      0 0 28px var(--glow-pink),
      0 0 46px var(--glow-magenta),
      0 0 70px var(--glow-magenta);
  }
  .sign__tagline {
    position: absolute;
    left: 0;
    right: 0;
    top: 174px;
    margin: 0;
    text-align: center;
    font-family: "Oswald", "Arial Narrow", sans-serif;
    font-weight: 500;
    font-size: 41px;
    line-height: 1;
    letter-spacing: 0.3px;
    color: var(--title-white);
  }
</style>
</head>
<body>
<div class="sign">
  <div class="sign__panel"></div>

  <svg class="sign__art" width="1200" height="255" viewBox="0 0 1200 255">
    <defs>
      <linearGradient id="bottleGlass" x1="0" y1="0" x2="1" y2="0">
        <stop offset="0" stop-color="var(--bottle-green-dark)"/>
        <stop offset="0.5" stop-color="var(--bottle-green)"/>
        <stop offset="1" stop-color="var(--bottle-green-dark)"/>
      </linearGradient>
      <radialGradient id="beerSpray" cx="0.5" cy="0.5" r="0.5">
        <stop offset="0" stop-color="var(--spray-foam)" stop-opacity="0.85"/>
        <stop offset="0.6" stop-color="var(--spray-amber)" stop-opacity="0.55"/>
        <stop offset="1" stop-color="var(--spray-amber)" stop-opacity="0"/>
      </radialGradient>
    </defs>

    <g class="bottle bottle--left">
      <ellipse class="bottle__spray" cx="168" cy="72" rx="52" ry="66"
               fill="url(#beerSpray)" role="img"
               aria-label="Beer and foam squirting from the popped bottle"/>
      <rect class="bottle__body" x="52" y="108" width="40" height="140" rx="14"
            transform="rotate(32 72 178)" fill="url(#bottleGlass)" role="img"
            aria-label="Green Kauriheld beer bottle with the cap popping"/>
    </g>

    <g class="bottle bottle--right">
      <ellipse class="bottle__spray" cx="1030" cy="72" rx="52" ry="66"
               fill="url(#beerSpray)" role="img"
               aria-label="Beer and foam squirting from the popped bottle"/>
      <rect class="bottle__body" x="1108" y="108" width="40" height="140" rx="14"
            transform="rotate(-32 1128 178)" fill="url(#bottleGlass)" role="img"
            aria-label="Green Kauriheld beer bottle with the cap popping"/>
    </g>
  </svg>

  <h1 class="sign__title">Ned's Bar</h1>
  <p class="sign__tagline">What happens in the bar stays in the bar</p>
</div>
</body>
</html>
```